Million Dollar Vehicle Design For Home Service Company

New design for Bright-Path Servicemen (home service company) vehicles.

Both sides and back

We are a new (opening in about 30 days) home service company.

We will begin by offering residential electrical services and soon expand to a full line by adding handyman, heating, cooling. plumbing and drain cleaning.

Looking for simple. Not cluttered.

Minimalist - Less is More mindset, but it must catch the eye.

Here is a link the website prototype being built for us. It has a bit more stuff on it now than it will in its final version, but this will help you get a feel for the colors.

http://www.lanternquaydigital.com/PROOF/brightpath-servicemen-4/

You may also find inspiration at cozyvantrel.com

**Also, please note that some of the attached files will differ from my requests due to changes being made as we get closer to opening. For example, the tagline is different.

Target Market(s)

Home Owners 35 - 65 years old.

Industry/Entity Type

Electrician

Font styles to use
Serif

Requirements
Must have
• Simple. Easy to read. Easy to understand what the company does and how to contact.
• Big Website
• Big Phone Number
• Big Name
• Website: MyBrightPathPro.com
• Phone number: 555-014-2287
• ***Tagline: Bright-Path, Each Visit or You'll Save $39
• ***Please note the tagline in this brief is different than is in the attached image.
Nice to have
• We will be adding services in the future. It would be nice to consider how these will be displayed on the vehicle. For example, it should be listed that we provide expert electrical services. I want to be able to list other services such as plumbing, heating and cooling as we add them by modifying only few things on each vehicle.
Should not have
• Cluttered. Should not be difficult to understand within 1 second.

```html
<!DOCTYPE html>
<html lang="en">
<head>
<meta charset="utf-8">
<title>Bright-Path Servicemen – Vehicle Wrap Layout</title>
<link rel="stylesheet" href="https://fonts.googleapis.com/css2?family=Oswald:wght@700&family=Open+Sans:ital,wght@1,700;1,800&display=swap">
<style>
  :root {
    --backdrop: #2f4a27;
    --wrap-orange: #e9521f;
    --wrap-white: #ffffff;
    --stripe-grey: #b9b9b9;
    --ink: #1b1b1b;
    --tick-green: #5c9a2b;
    --figure-red: #d9472a;
    --figure-blue: #2c4f9e;
  }
  * { margin: 0; padding: 0; box-sizing: border-box; }
  html, body { width: 878px; height: 1200px; overflow: hidden; }
  body { background: var(--backdrop); position: relative; }
  .wrap-panel { position: absolute; display: block; }
  .panel-driver { left: 19px; top: 40px; width: 840px; height: 306px; }
  .panel-passenger { left: 19px; top: 380px; width: 840px; height: 306px; }
  .panel-rear { left: 200px; top: 740px; width: 500px; height: 398px; }
  .brand-name { font-family: "Oswald", sans-serif; font-weight: 700; fill: var(--wrap-orange); letter-spacing: 0.5px; }
  .service-tag { font-family: "Open Sans", sans-serif; font-weight: 800; font-style: italic; fill: var(--wrap-white); }
  .service-list { font-family: "Open Sans", sans-serif; font-weight: 800; font-style: italic; fill: var(--ink); }
  .tagline { font-family: "Open Sans", sans-serif; font-weight: 700; font-style: italic; fill: var(--ink); }
  .tagline .price { fill: var(--tick-green); }
  .web-label { font-family: "Open Sans", sans-serif; font-weight: 800; font-style: italic; fill: var(--wrap-white); }
  .phone-label { font-family: "Open Sans", sans-serif; font-weight: 800; fill: var(--wrap-white); }
  .tick { fill: none; stroke: var(--tick-green); stroke-width: 2.4; stroke-linecap: round; stroke-linejoin: round; }
</style>
</head>
<body>

<svg width="0" height="0" style="position:absolute">
  <defs>
    <path id="van-side-outline" d="M0,170 L40,150 L100,40 Q115,8 150,5 L712,5 Q732,6 734,28 L736,210 L708,210 Q698,182 632,180 Q566,182 556,215 L552,252 L242,256 L226,246 Q212,196 160,196 Q108,196 100,244 L8,236 Z"/>
    <clipPath id="van-side-clip"><use href="#van-side-outline"/></clipPath>
    <linearGradient id="figure-fill" x1="0" y1="0" x2="0" y2="1">
      <stop offset="0" stop-color="var(--figure-red)"/>
      <stop offset="0.5" stop-color="#e8773f"/>
      <stop offset="1" stop-color="var(--figure-blue)"/>
    </linearGradient>
  </defs>
</svg>

<!-- Driver side: cab on the left -->
<svg class="wrap-panel panel-driver" viewBox="0 0 740 270">
  <g class="van-body" clip-path="url(#van-side-clip)">
    <rect width="740" height="270" fill="var(--wrap-orange)"/>
    <path d="M250,0 C270,140 360,220 500,270 L740,270 L740,0 Z" fill="var(--stripe-grey)"/>
    <path d="M262,0 C282,138 372,216 516,270 L740,270 L740,0 Z" fill="var(--wrap-white)"/>
    <path class="window-opening" d="M112,44 Q124,22 150,22 L238,22 Q250,22 250,36 L250,100 L98,100 Z" fill="var(--backdrop)"/>
    <rect class="sill-opening" x="240" y="224" width="290" height="10" fill="var(--backdrop)"/>
    <rect x="232" y="118" width="6" height="16" rx="2" fill="var(--backdrop)"/>
  </g>
  <g class="services">
    <path class="tick" d="M320,93 l4,5 l8,-11"/>
    <text class="service-list" x="336" y="99" font-size="14">PLUMBING</text>
    <path class="tick" d="M320,110 l4,5 l8,-11"/>
    <text class="service-list" x="336" y="116" font-size="14">HEATING</text>
    <path class="tick" d="M320,127 l4,5 l8,-11"/>
    <text class="service-list" x="336" y="133" font-size="14">COOLING</text>
  </g>
  <g class="contact" transform="rotate(-5 360 170)">
    <rect x="290" y="138" width="160" height="22" rx="3" fill="var(--wrap-orange)"/>
    <text class="web-label" x="370" y="154" font-size="14" text-anchor="middle">MyBrightPathPro.com</text>
    <rect x="286" y="162" width="170" height="30" rx="4" fill="var(--ink)"/>
    <text class="phone-label" x="371" y="185" font-size="22" text-anchor="middle">555-014-2287</text>
  </g>
  <rect class="mascot-art" role="img" aria-label="Illustration of two cartoon technicians in orange caps and shirts with tool belts" x="452" y="16" width="106" height="156" rx="10" fill="url(#figure-fill)"/>
  <g class="brand-block">
    <text class="brand-name" x="566" y="62" font-size="30">Bright-Path</text>
    <text class="brand-name" x="566" y="96" font-size="30">Servicemen</text>
    <rect x="566" y="104" width="150" height="20" fill="var(--ink)"/>
    <text class="service-tag" x="641" y="119" font-size="13" text-anchor="middle">ELECTRICIANS</text>
    <text class="tagline" x="641" y="142" font-size="10" text-anchor="middle">Bright-Path, each visit</text>
    <text class="tagline" x="641" y="155" font-size="10" text-anchor="middle">or you'll save <tspan class="price">$39</tspan>!</text>
  </g>
</svg>

<!-- Passenger side: cab on the right -->
<svg class="wrap-panel panel-passenger" viewBox="0 0 740 270">
  <g class="van-body" transform="translate(740 0) scale(-1 1)">
    <g clip-path="url(#van-side-clip)">
      <rect width="740" height="270" fill="var(--wrap-orange)"/>
      <path d="M250,0 C270,140 360,220 500,270 L740,270 L740,0 Z" fill="var(--stripe-grey)"/>
      <path d="M262,0 C282,138 372,216 516,270 L740,270 L740,0 Z" fill="var(--wrap-white)"/>
      <path class="window-opening" d="M112,44 Q124,22 150,22 L238,22 Q250,22 250,36 L250,100 L98,100 Z" fill="var(--backdrop)"/>
      <rect class="sill-opening" x="240" y="224" width="290" height="10" fill="var(--backdrop)"/>
      <rect x="232" y="118" width="6" height="16" rx="2" fill="var(--backdrop)"/>
    </g>
  </g>
  <rect class="mascot-art" role="img" aria-label="Illustration of two cartoon technicians in orange caps and shirts with tool belts" x="36" y="16" width="106" height="156" rx="10" fill="url(#figure-fill)"/>
  <g class="brand-block">
    <text class="brand-name" x="150" y="62" font-size="30">Bright-Path</text>
    <text class="brand-name" x="150" y="96" font-size="30">Servicemen</text>
    <rect x="150" y="104" width="150" height="20" fill="var(--ink)"/>
    <text class="service-tag" x="225" y="119" font-size="13" text-anchor="middle">ELECTRICIANS</text>
    <text class="tagline" x="225" y="142" font-size="10" text-anchor="middle">Bright-Path, each visit</text>
    <text class="tagline" x="225" y="155" font-size="10" text-anchor="middle">or you'll save <tspan class="price">$39</tspan>!</text>
  </g>
  <g class="services">
    <path class="tick" d="M322,98 l4,5 l8,-11"/>
    <text class="service-list" x="338" y="104" font-size="14">PLUMBING</text>
    <path class="tick" d="M322,115 l4,5 l8,-11"/>
    <text class="service-list" x="338" y="121" font-size="14">HEATING</text>
    <path class="tick" d="M322,132 l4,5 l8,-11"/>
    <text class="service-list" x="338" y="138" font-size="14">COOLING</text>
  </g>
  <g class="contact" transform="rotate(-5 390 190)">
    <rect x="312" y="160" width="160" height="22" rx="3" fill="var(--wrap-orange)"/>
    <text class="web-label" x="392" y="176" font-size="14" text-anchor="middle">MyBrightPathPro.com</text>
    <rect x="308" y="184" width="170" height="30" rx="4" fill="var(--ink)"/>
    <text class="phone-label" x="393" y="207" font-size="22" text-anchor="middle">555-014-2287</text>
  </g>
</svg>

<!-- Rear doors -->
<svg class="wrap-panel panel-rear" viewBox="0 0 270 215">
  <path class="rear-body" d="M12,8 Q14,2 24,2 L246,2 Q258,2 260,10 L262,26 L268,30 L268,100 L264,104 L264,210 L6,210 L6,104 L2,100 L2,30 L8,26 Z" fill="var(--wrap-white)"/>
  <rect class="handle-opening" x="14" y="148" width="100" height="5" fill="var(--backdrop)"/>
  <rect class="mascot-art" role="img" aria-label="Illustration of two cartoon technicians in orange caps and shirts with tool belts" x="16" y="26" width="68" height="112" rx="8" fill="url(#figure-fill)"/>
  <g class="brand-block">
    <text class="brand-name" x="89" y="58" font-size="19">Bright-Path</text>
    <text class="brand-name" x="89" y="79" font-size="19">Servicemen</text>
    <rect x="89" y="84" width="88" height="13" fill="var(--ink)"/>
    <text class="service-tag" x="133" y="94" font-size="8" text-anchor="middle">ELECTRICIANS</text>
  </g>
  <text class="tagline" x="194" y="46" font-size="7">Bright-Path, each</text>
  <text class="tagline" x="194" y="55" font-size="7">visit, save <tspan class="price">$39</tspan>!</text>
  <g class="services">
    <path class="tick" d="M178,106 l2.5,3 l5,-7" style="stroke-width:1.6"/>
    <text class="service-list" x="188" y="110" font-size="8.5">PLUMBING</text>
    <path class="tick" d="M178,117 l2.5,3 l5,-7" style="stroke-width:1.6"/>
    <text class="service-list" x="188" y="121" font-size="8.5">HEATING</text>
    <path class="tick" d="M178,128 l2.5,3 l5,-7" style="stroke-width:1.6"/>
    <text class="service-list" x="188" y="132" font-size="8.5">COOLING</text>
  </g>
  <g class="contact" transform="rotate(-3 200 170)">
    <rect x="140" y="148" width="116" height="15" rx="2" fill="var(--wrap-orange)"/>
    <text class="web-label" x="198" y="159" font-size="9.5" text-anchor="middle">MyBrightPathPro.com</text>
    <rect x="136" y="165" width="122" height="21" rx="3" fill="var(--ink)"/>
    <text class="phone-label" x="197" y="181" font-size="15" text-anchor="middle">555-014-2287</text>
  </g>
</svg>

</body>
</html>
```